Plant Grower/Nursery needs a fun, professional and fresh 1/2 page print ad for a high profile gar...

We need a print ad for a garden tour geared towards plant enthusiasts that support California Native, natural and sustainable plants. A good percentage of our target market want a conservation and earth friendly approach to gardens/landscaping. We want to target this market, as well as, people who are looking for a pretty/colorful landscape that require little water/maintenance. **PLEASE LET US KNOW IF YOU HAVE QUESTIONS OR NEED MORE INFORMATION. WE ALSO HAVE MANY MORE PICTURES IF THESE DON'T WORK FOR YOUR DESIGN. ***THE AD CAN HAVE AS FEW AS 1 PHOTO - WE ARE POSTING SEVERAL IN HOPES THAT YOU CAN FIND WHAT IS PERFECT FOR YOUR IDEA!!Thank you

Target Market(s)

Gardeners, Landscapers, Landscape Designers/Architects, Cities and Municipalities.

Industry/Entity Type

Agriculture

Font styles to use
Serif
Sans Serif

Colors

Requirements
Must have
• We believe in growing regionally appropriate plants for Southern California that beatify our natural and urban landscapes.
• For over 20 years, our owners and staff take pride in providing timely, expert, and honest service.
Nice to have
• At least 1 photo. Eye catchy with a modern earthy feel.
• Hundreds of species/hybrids in stock of California Natives, Succulents, Ornamental Grasses, Standard Stock Items and Unique Plants.

```html
<!DOCTYPE html>
<html lang="en">
<head>
<meta charset="utf-8">
<title>Native Plants Garden Tour Ad</title>
<link rel="stylesheet" href="https://fonts.googleapis.com/css2?family=Montserrat:wght@600;700&display=swap">
<style>
  :root {
    --page-bg: #e9e9e9;
    --forest: #2f7a3d;
    --leaf: #4c9a3c;
    --lime: #a6e619;
    --swoosh: #8fd14a;
    --ink: #2e2e2e;
    --white: #ffffff;
    --grass-dark: #4f9a16;
    --grass-light: #8ed42a;
  }
  * { margin: 0; padding: 0; box-sizing: border-box; }
  html, body {
    width: 1200px; height: 1200px; overflow: hidden;
    background: var(--page-bg);
    font-family: "Montserrat", Arial, sans-serif;
  }
  .ad {
    position: absolute; left: 2px; top: 179px;
    width: 1196px; height: 842px; overflow: hidden;
    background: var(--white);
  }
  .ad__photo {
    position: absolute; inset: 0;
    background:
      radial-gradient(ellipse 260px 240px at 520px 420px, rgba(214, 60, 170, 0.85), rgba(214, 60, 170, 0) 70%),
      linear-gradient(120deg, #6e8a55 0%, #8aa36f 35%, #5f7d4a 60%, #93ab84 80%, #6a8656 100%);
  }
  .ad__shapes { position: absolute; inset: 0; width: 1196px; height: 842px; }
  .ad__grass {
    position: absolute; left: 0; top: 766px; width: 980px; height: 76px;
    background: linear-gradient(180deg, var(--grass-light) 0%, var(--grass-dark) 100%);
    clip-path: polygon(0 0, 100% 0, 100% 100%, 0 100%);
    -webkit-mask: linear-gradient(90deg, #000 90%, transparent 100%);
            mask: linear-gradient(90deg, #000 90%, transparent 100%);
  }
  .headline {
    position: absolute; left: 0; top: 44px; width: 1196px;
    text-align: center; padding-left: 4px;
    font-weight: 700; font-size: 39px; line-height: 46px; letter-spacing: 0.5px;
  }
  .headline__line--white { color: var(--white); }
  .headline__line--lime { color: var(--lime); font-size: 44px; }
  .tagline {
    position: absolute; left: 0; top: 146px; width: 1196px; padding-left: 4px;
    text-align: center; color: var(--white);
    font-weight: 700; font-size: 18.5px; line-height: 24px;
  }
  .mission {
    position: absolute; left: 76px; top: 684px; width: 620px;
    text-align: center; color: var(--ink);
    font-weight: 700; font-size: 18.5px; line-height: 24px;
  }
</style>
</head>
<body>
  <section class="ad">
    <div class="ad__photo" role="img" aria-label="Close-up photo of a magenta flower spike among soft grey-green leaves"></div>

    <svg class="ad__shapes" viewBox="0 0 1196 842" aria-hidden="true">
      <defs>
        <linearGradient id="topBand" x1="0" y1="0" x2="0" y2="1">
          <stop offset="0" stop-color="#2f7a3d"/>
          <stop offset="1" stop-color="#4f9a3e"/>
        </linearGradient>
        <linearGradient id="cornerFade" x1="0" y1="0" x2="1" y2="1">
          <stop offset="0" stop-color="#6fae5a" stop-opacity="0"/>
          <stop offset="1" stop-color="#8cc275" stop-opacity="0.45"/>
        </linearGradient>
      </defs>

      <!-- top band -->
      <path d="M0 0 H1196 V100 C1000 190 780 262 600 262 C380 262 180 200 0 108 Z" fill="url(#topBand)"/>
      <path d="M920 0 H1196 V100 C1120 140 1040 170 960 190 Z" fill="url(#cornerFade)"/>
      <path d="M1196 100 C1000 190 780 262 600 262" fill="none" stroke="#8bbf3c" stroke-width="2"/>
      <!-- swoosh -->
      <path d="M0 106 C160 185 340 228 536 216 C360 232 170 200 0 126 Z" fill="var(--swoosh)"/>
      <path d="M0 116 C170 190 350 226 536 216" fill="none" stroke="#ffffff" stroke-width="1.5" opacity="0.8"/>

      <!-- bottom band -->
      <path d="M0 666 C170 600 340 574 500 576 C760 580 940 700 1070 842 H0 Z" fill="var(--forest)"/>
      <path d="M0 690 C170 630 340 606 470 608" fill="none" stroke="#9ad14b" stroke-width="3"/>
      <path d="M0 705 C160 650 320 612 470 612 C680 612 860 730 970 842 H0 Z" fill="var(--white)"/>
    </svg>

    <div class="ad__grass" role="img" aria-label="Illustrated strip of green grass blades"></div>

    <h1 class="headline">
      <span class="headline__line--white">CALIFORNIA NATIVE, NATURAL</span><br>
      <span class="headline__line--lime">AND SUSTAINABLE PLANTS</span>
    </h1>

    <p class="tagline">For over 20 years, our owners and staff take pride in<br>providing timely, expert, and honest service.</p>

    <p class="mission">We believe in growing regionally appropriate plants for Southern California that beatify our natural and urban landscapes.</p>
  </section>
</body>
</html>
```